Global Beard Oil Review Business needs a refresh

topwhiskertonic.net is a global business who's mission is to curate all available beard oils from around the world, review and grade them and present this curated collection to the user of the website.

The scope of this job includes the web site design and the design of a suitable logo to be used in the site header.

The existing site can be seen on http://topwhiskertonic.net, however this is a mock-up only the style and logo should NOT be used. This is to give you an idea of the concept of the site only.

This job is for PSD design only.

See attached design brief for detailed design requirements.
Updates

Project Deadline Extended
Reason: Extending deadline by 5 days to allow for final submissions

Target Market(s)

Men's grooming / retail

Industry/Entity Type

Retail

Number of Pages Required

2 page

Font styles to use
Sans Serif

Requirements
Must have
• 1) Comparison Table
• 2) Side Bar
• 3) Header area
• 4) Photo of Calvin Dorrow (attached - can be circular or "cut-out")
• 5) Cool beard-oriented custom design background (e.g., stylistic black/brown on brown/orange beard background. I envision this beard background "drawing" rather than photo based)
• (see attached design requirements for details)
Nice to have
• Signature style writing at top with name "Calvin Dorrow"
Should not have
• Do NOT use the look & feel or logo from the existing site.

```html
<!DOCTYPE html>
<html lang="en">
<head>
<meta charset="utf-8">
<title>Top Whisker Tonic</title>
<link href="https://fonts.googleapis.com/css2?family=Amatic+SC:wght@700&family=Open+Sans:wght@400;600;700&family=Raleway:wght@400;500;600&family=Kaushan+Script&display=swap" rel="stylesheet">
<style>
:root{
  --orange:#ffb20f;
  --hero:#ffcd5c;
  --cream:#fdf1d8;
  --maroon:#5e0b0b;
  --ink:#2a2a2a;
  --grey:#d6d6d6;
  --line:#dcdcdc;
  --white:#ffffff;
}
*{box-sizing:border-box;margin:0;padding:0}
html,body{width:1200px;height:2557px;overflow:hidden}
body{position:relative;font-family:"Open Sans",Arial,sans-serif;color:var(--ink);background:var(--grey)}
.beard-backdrop{position:absolute;inset:0;background:
  radial-gradient(circle at 20% 15%,#f4f4f4 0,#cfcfcf 35%,transparent 60%),
  radial-gradient(circle at 85% 45%,#f0f0f0 0,#c8c8c8 40%,transparent 65%),
  radial-gradient(circle at 15% 80%,#eeeeee 0,#c4c4c4 40%,transparent 65%),
  linear-gradient(135deg,#e4e4e4,#bdbdbd 50%,#e2e2e2)}
.page{position:absolute;left:60px;top:0;width:1079px;height:2514px;background:var(--white)}
.abs{position:absolute}

/* header */
.brand{left:78px;top:46px;display:flex;align-items:center;gap:10px;font-family:"Raleway",sans-serif;font-weight:600;font-size:21px;color:var(--maroon);white-space:nowrap}
.brand-dot{width:26px;height:26px;border-radius:50%;background:var(--orange);flex:none}
.avatar{left:322px;top:0;width:160px;height:160px;border-radius:50%;border:6px solid var(--white);box-shadow:0 2px 6px rgba(0,0,0,.25);background:radial-gradient(circle at 50% 40%,#8a8a8a,#3a3a3a)}
.signature{left:486px;top:24px;font-family:"Kaushan Script",cursive;font-size:25px;color:var(--ink);border-bottom:2px solid var(--ink);padding:0 6px 2px}
.contact{left:741px;top:30px;display:flex;align-items:center;gap:9px;font-size:14px}
.mail-ico{width:26px;height:26px;border-radius:50%;background:var(--orange);display:flex;align-items:center;justify-content:center}
.socials{display:flex;gap:9px}
.socials span{width:26px;height:26px;border-radius:50%;background:var(--orange);display:block}
.socials.top{left:984px;top:30px}
.nav{left:520px;top:85px;width:619px;height:38px;background:#f2f2f2;display:flex;align-items:center;font-family:"Raleway",sans-serif;font-size:16px;color:#333}
.nav a{color:inherit;text-decoration:none;padding:0 9px}
.nav a.active{background:var(--maroon);color:var(--white);padding:5px 14px;margin-right:14px}
.nav .sep{width:4px;height:4px;background:#555;border-radius:50%}

/* hero */
.hero{left:80px;top:136px;width:1040px;height:409px;background:var(--hero);overflow:hidden}
.hero-disc{position:absolute;left:235px;top:52px;width:310px;height:310px;border-radius:50%;background:var(--cream)}
.hero-disc .tag{position:absolute;left:95px;top:110px;font-family:"Raleway",sans-serif;font-weight:600;font-size:19px;color:var(--maroon);white-space:nowrap}
.hero-disc .with{position:absolute;left:110px;top:148px;font-family:"Kaushan Script",cursive;font-size:19px;white-space:nowrap}
.hero-person{position:absolute;left:36px;top:0;width:276px;height:409px;background:linear-gradient(180deg,#8c6a55,#4d4d4d)}
.hero h1{position:absolute;left:597px;top:82px;width:430px;font-family:"Amatic SC",sans-serif;font-size:60px;line-height:1.15;color:var(--ink);font-weight:700}
.btn{display:inline-block;background:var(--orange);color:var(--ink);font-family:"Raleway",sans-serif}
.hero .btn{position:absolute;left:597px;top:270px;width:141px;height:52px;line-height:52px;text-align:center;font-size:24px}
.dots{position:absolute;left:601px;top:339px;display:flex;gap:7px}
.dots i{width:7px;height:7px;border-radius:50%;background:var(--white);display:block}
.dots i.on{background:var(--orange)}

/* welcome */
.welcome{left:80px;top:570px;width:1040px;text-align:center}
.welcome h2{font-family:"Amatic SC",sans-serif;font-size:66px;font-weight:700;color:var(--ink)}
.welcome h2 em{font-style:normal;color:var(--maroon)}
.welcome p{width:900px;margin:6px auto 0;font-size:13px;line-height:21px}
.steps{left:80px;top:770px;width:1040px;height:180px}
.step{position:absolute;width:170px;text-align:center;font-family:"Amatic SC",sans-serif;font-size:30px;font-weight:700}
.step .disc{width:110px;height:110px;border-radius:50%;background:var(--orange);margin:0 auto 8px;display:flex;align-items:center;justify-content:center}

/* table */
.reviews{left:80px;top:985px;width:781px;border-collapse:collapse;table-layout:fixed;font-size:13px}
.reviews th{background:var(--maroon);color:var(--orange);font-weight:700;font-size:13px;height:63px;text-align:left;padding:0 8px;vertical-align:middle}
.reviews th.rate{background:var(--orange);color:var(--maroon);font-size:10px;text-align:center;padding:0 2px;line-height:1.2}
.reviews th .pick{display:inline-block;background:var(--white);color:var(--ink);font-size:10px;font-weight:400;padding:1px 4px;margin-left:4px}
.reviews td{height:90px;border-right:1px solid var(--line);text-align:center;vertical-align:middle;padding:0 4px}
.reviews td:last-child{border-right:none}
.reviews td.product{text-align:left;padding-left:12px}
.product-cell{display:flex;align-items:center;gap:10px}
.thumb{width:36px;height:56px;flex:none;background:linear-gradient(180deg,#f4e3b0,#c98a1c)}
.thumb.dark{background:linear-gradient(180deg,#e8d6c8,#6b3b23)}
.pname{color:var(--maroon);font-weight:700;font-size:15px;line-height:1.25}
.maker{font-size:12.5px;color:#444}
.buy{background:var(--orange);color:var(--white);font-size:12.5px;padding:5px 6px;font-weight:600}
.loading{left:395px;top:2450px;width:150px;height:33px;background:#3a3a3a;color:var(--white);font-size:14px;border-radius:3px;display:flex;align-items:center;justify-content:center;gap:8px}

/* sidebar */
.subscribe{left:885px;top:985px;width:235px;height:345px;background:var(--orange);text-align:center;padding:20px 16px}
.subscribe h3{font-family:"Amatic SC",sans-serif;font-size:32px;line-height:1.15;color:var(--maroon);font-weight:700}
.subscribe p{font-size:12.5px;line-height:1.45;margin-top:12px;color:var(--ink)}
.subscribe .field{margin:16px auto 0;height:36px;background:var(--white);font-size:11.5px;color:#999;line-height:36px}
.subscribe .signup{margin-top:12px;height:36px;line-height:36px;background:var(--maroon);color:var(--white);font-weight:700;font-size:14px}
.subscribe small{display:block;margin-top:14px;font-size:10px;color:var(--maroon);line-height:1.4}
.blog-title{left:885px;top:1378px;font-family:"Amatic SC",sans-serif;font-size:38px;color:var(--maroon);font-weight:700}
.post{position:absolute;left:885px;width:235px}
.post .shot{height:154px;background:linear-gradient(135deg,#c98a4c,#8a5a32)}
.post h4{margin-top:10px;color:var(--orange);font-size:14px;line-height:1.2;font-weight:700}
.post time{font-size:12.5px;color:var(--ink)}

/* footer */
.footer{left:0;top:2514px;width:1200px;height:43px;background:var(--orange);display:flex;align-items:center;justify-content:space-between;padding:0 80px;font-size:13.5px;color:var(--white)}
.footer .socials span{background:transparent;border:2px solid var(--white)}
</style>
</head>
<body>
<div class="beard-backdrop" role="img" aria-label="Grey background pattern of drawn bearded faces"></div>
<div class="page"></div>

<header>
  <div class="abs brand"><span class="brand-dot"></span>Top Whisker Tonic</div>
  <div class="abs avatar" role="img" aria-label="Circular portrait photo of Calvin Dorrow"></div>
  <div class="abs signature">Calvin Dorrow</div>
  <div class="abs contact">
    <span class="mail-ico"><svg width="14" height="10" viewBox="0 0 14 10"><rect x="0.5" y="0.5" width="13" height="9" fill="none" stroke="#5e0b0b"/><path d="M0.5 0.5 7 5.5 13.5 0.5" fill="none" stroke="#5e0b0b"/></svg></span>
    info@topwhiskertonic.net
  </div>
  <div class="abs socials top" aria-label="Social links"><span></span><span></span><span></span><span></span></div>
  <nav class="abs nav">
    <a class="active" href="#">Home</a>
    <a href="#">About</a><span class="sep"></span>
    <a href="#">Our Charter</a><span class="sep"></span>
    <a href="#">Beard Oil Review Methodology</a><span class="sep"></span>
    <a href="#">Blog</a>
  </nav>
</header>

<section class="abs hero">
  <div class="hero-disc"><span class="tag">Top Whisker Tonic</span><span class="with">-With Calvin Dorrow</span></div>
  <div class="hero-person" role="img" aria-label="Photo of a bearded man giving a thumbs up and holding a beard oil bottle"></div>
  <h1>Curate, Review &amp; Grade<br>Then Present</h1>
  <a class="btn">See Table</a>
  <div class="dots"><i></i><i></i><i></i><i class="on"></i></div>
</section>

<section class="abs welcome">
  <h2>Welcome To <em>Top Whisker Tonic</em></h2>
  <p>We are a global business with the mission is to curate all available beard oils from around the world, review &amp; grade them &amp; present this curated collection to the users of the site. Our Target Audience are all grooming men. Lorem ipsum dolor sit amet, consectetuer adipiscing elit, sed diam nonummy nibh euismod tincidunt ut laoreet dolore magna aliquam erat volutpat. Lorem ipsum dolor sit amet, consectetuer adipiscing elit, sed diam nonummy nibh euismod tincidunt ut laoreet dolore magna aliquam erat volutpat.</p>
</section>

<section class="abs steps">
  <svg class="abs" style="left:0;top:0" width="1040" height="180" viewBox="0 0 1040 180">
    <path id="arcA" d="M205 70 Q335 150 465 80" fill="none" stroke="#5e0b0b" stroke-width="1.5" stroke-dasharray="2 4"/>
    <path id="arcB" d="M575 55 Q705 -15 840 55" fill="none" stroke="#5e0b0b" stroke-width="1.5" stroke-dasharray="2 4"/>
    <text font-family="Open Sans, sans-serif" font-size="12" fill="#5e0b0b" dy="-6"><textPath href="#arcA" startOffset="10%">We curate all available beard oils</textPath></text>
    <text font-family="Open Sans, sans-serif" font-size="12" fill="#5e0b0b" dy="-6"><textPath href="#arcB" startOffset="8%">Review &amp; Grade them &amp; Present</textPath></text>
  </svg>
  <div class="step" style="left:62px;top:15px"><div class="disc"><svg width="50" height="50" viewBox="0 0 50 50"><path d="M10 26 20 36 40 14" fill="none" stroke="#5e0b0b" stroke-width="6" stroke-linecap="round" stroke-linejoin="round"/></svg></div>Curate</div>
  <div class="step" style="left:435px;top:15px"><div class="disc"><svg width="54" height="54" viewBox="0 0 24 24"><path d="M12 2l3 6.5 7 .8-5.2 4.8 1.4 7L12 17.6 5.8 21.1l1.4-7L2 9.3l7-.8z" fill="#5e0b0b"/></svg></div>Review &amp; Grade</div>
  <div class="step" style="left:808px;top:15px"><div class="disc"><svg width="52" height="48" viewBox="0 0 52 48"><rect x="3" y="3" width="46" height="34" fill="none" stroke="#5e0b0b" stroke-width="4"/><path d="M26 44V20M17 28l9-9 9 9" fill="none" stroke="#5e0b0b" stroke-width="4"/></svg></div>Present</div>
</section>

<table class="abs reviews">
  <colgroup><col style="width:189px"><col style="width:77px"><col style="width:85px"><col style="width:103px"><col style="width:49px"><col style="width:48px"><col style="width:46px"><col style="width:44px"><col style="width:80px"><col style="width:60px"></colgroup>
  <thead><tr>
    <th>Product Supplier <span class="pick">Bristle Baron ▼</span></th>
    <th>Origin ▼</th><th>Base Oil ▼</th><th>Scent ▼</th>
    <th class="rate">Aroma<br>▼</th><th class="rate">Thera. Affect<br>▼</th><th class="rate">Value<br>▼</th><th class="rate">Over All<br>▼</th><th class="rate">Get It</th><th class="rate">Calvin Dorrow Recommend</th>
  </tr></thead>
  <tbody>
    <tr><td class="product"><div class="product-cell"><span class="thumb" role="img" aria-label="Product photo"></span><div><div class="pname">Ridge-Ranger</div><div class="maker">-Bristle Baron</div></div></div></td><td>USA</td><td>Jojoba,</td><td>Spice Market</td><td>5</td><td>5</td><td>5</td><td>5</td><td><span class="buy">Buy Now</span></td><td><svg width="18" height="18" viewBox="0 0 24 24"><path d="M2 10h4v12H2zM8 22h10l3-9v-3h-7l1-5-2-3-5 8z" fill="#5e0b0b"/></svg></td></tr>
    <tr><td class="product"><div class="product-cell"><span class="thumb dark" role="img" aria-label="Product photo"></span><div><div class="pname">Harbor Lane Tobacco</div><div class="maker">-Bristle Baron</div></div></div></td><td>USA</td><td>Jojoba,</td><td>Spice Market</td><td>5</td><td>5</td><td>5</td><td>5</td><td><span class="buy">Buy Now</span></td><td><svg width="18" height="18" viewBox="0 0 24 24"><path d="M2 10h4v12H2zM8 22h10l3-9v-3h-7l1-5-2-3-5 8z" fill="#5e0b0b"/></svg></td></tr>
    <tr><td class="product"><div class="product-cell"><span class="thumb" role="img" aria-label="Product photo"></span><div><div class="pname">Ridge-Ranger</div><div class="maker">-Bristle Baron</div></div></div></td><td>USA</td><td>Jojoba,</td><td>Spice Market</td><td>5</td><td>5</td><td>5</td><td>5</td><td><span class="buy">Buy Now</span></td><td><svg width="18" height="18" viewBox="0 0 24 24"><path d="M2 10h4v12H2zM8 22h10l3-9v-3h-7l1-5-2-3-5 8z" fill="#5e0b0b"/></svg></td></tr>
    <tr><td class="product"><div class="product-cell"><span class="thumb dark" role="img" aria-label="Product photo"></span><div><div class="pname">Harbor Lane Tobacco</div><div class="maker">-Bristle Baron</div></div></div></td><td>USA</td><td>Jojoba,</td><td>Spice Market</td><td>5</td><td>5</td><td>5</td><td>5</td><td><span class="buy">Buy Now</span></td><td><svg width="18" height="18" viewBox="0 0 24 24"><path d="M2 10h4v12H2zM8 22h10l3-9v-3h-7l1-5-2-3-5 8z" fill="#5e0b0b"/></svg></td></tr>
    <tr><td class="product"><div class="product-cell"><span class="thumb" role="img" aria-label="Product photo"></span><div><div class="pname">Ridge-Ranger</div><div class="maker">-Bristle Baron</div></div></div></td><td>USA</td><td>Jojoba,</td><td>Spice Market</td><td>5</td><td>5</td><td>5</td><td>5</td><td><span class="buy">Buy Now</span></td><td><svg width="18" height="18" viewBox="0 0 24 24"><path d="M2 10h4v12H2zM8 22h10l3-9v-3h-7l1-5-2-3-5 8z" fill="#5e0b0b"/></svg></td></tr>
    <tr><td class="product"><div class="product-cell"><span class="thumb dark" role="img" aria-label="Product photo"></span><div><div class="pname">Harbor Lane Tobacco</div><div class="maker">-Bristle Baron</div></div></div></td><td>USA</td><td>Jojoba,</td><td>Spice Market</td><td>5</td><td>5</td><td>5</td><td>5</td><td><span class="buy">Buy Now</span></td><td><svg width="18" height="18" viewBox="0 0 24 24"><path d="M2 10h4v12H2zM8 22h10l3-9v-3h-7l1-5-2-3-5 8z" fill="#5e0b0b"/></svg></td></tr>
    <tr><td class="product"><div class="product-cell"><span class="thumb" role="img" aria-label="Product photo"></span><div><div class="pname">Ridge-Ranger</div><div class="maker">-Bristle Baron</div></div></div></td><td>USA</td><td>Jojoba,</td><td>Spice Market</td><td>5</td><td>5</td><td>5</td><td>5</td><td><span class="buy">Buy Now</span></td><td><svg width="18" height="18" viewBox="0 0 24 24"><path d="M2 10h4v12H2zM8 22h10l3-9v-3h-7l1-5-2-3-5 8z" fill="#5e0b0b"/></svg></td></tr>
    <tr><td class="product"><div class="product-cell"><span class="thumb dark" role="img" aria-label="Product photo"></span><div><div class="pname">Harbor Lane Tobacco</div><div class="maker">-Bristle Baron</div></div></div></td><td>USA</td><td>Jojoba,</td><td>Spice Market</td><td>5</td><td>5</td><td>5</td><td>5</td><td><span class="buy">Buy Now</span></td><td><svg width="18" height="18" viewBox="0 0 24 24"><path d="M2 10h4v12H2zM8 22h10l3-9v-3h-7l1-5-2-3-5 8z" fill="#5e0b0b"/></svg></td></tr>
    <tr><td class="product"><div class="product-cell"><span class="thumb" role="img" aria-label="Product photo"></span><div><div class="pname">Ridge-Ranger</div><div class="maker">-Bristle Baron</div></div></div></td><td>USA</td><td>Jojoba,</td><td>Spice Market</td><td>5</td><td>5</td><td>5</td><td>5</td><td><span class="buy">Buy Now</span></td><td><svg width="18" height="18" viewBox="0 0 24 24"><path d="M2 10h4v12H2zM8 22h10l3-9v-3h-7l1-5-2-3-5 8z" fill="#5e0b0b"/></svg></td></tr>
    <tr><td class="product"><div class="product-cell"><span class="thumb dark" role="img" aria-label="Product photo"></span><div><div class="pname">Harbor Lane Tobacco</div><div class="maker">-Bristle Baron</div></div></div></td><td>USA</td><td>Jojoba,</td><td>Spice Market</td><td>5</td><td>5</td><td>5</td><td>5</td><td><span class="buy">Buy Now</span></td><td><svg width="18" height="18" viewBox="0 0 24 24"><path d="M2 10h4v12H2zM8 22h10l3-9v-3h-7l1-5-2-3-5 8z" fill="#5e0b0b"/></svg></td></tr>
    <tr><td class="product"><div class="product-cell"><span class="thumb" role="img" aria-label="Product photo"></span><div><div class="pname">Ridge-Ranger</div><div class="maker">-Bristle Baron</div></div></div></td><td>USA</td><td>Jojoba,</td><td>Spice Market</td><td>5</td><td>5</td><td>5</td><td>5</td><td><span class="buy">Buy Now</span></td><td><svg width="18" height="18" viewBox="0 0 24 24"><path d="M2 10h4v12H2zM8 22h10l3-9v-3h-7l1-5-2-3-5 8z" fill="#5e0b0b"/></svg></td></tr>
    <tr><td class="product"><div class="product-cell"><span class="thumb dark" role="img" aria-label="Product photo"></span><div><div class="pname">Harbor Lane Tobacco</div><div class="maker">-Bristle Baron</div></div></div></td><td>USA</td><td>Jojoba,</td><td>Spice Market</td><td>5</td><td>5</td><td>5</td><td>5</td><td><span class="buy">Buy Now</span></td><td><svg width="18" height="18" viewBox="0 0 24 24"><path d="M2 10h4v12H2zM8 22h10l3-9v-3h-7l1-5-2-3-5 8z" fill="#5e0b0b"/></svg></td></tr>
    <tr><td class="product"><div class="product-cell"><span class="thumb" role="img" aria-label="Product photo"></span><div><div class="pname">Ridge-Ranger</div><div class="maker">-Bristle Baron</div></div></div></td><td>USA</td><td>Jojoba,</td><td>Spice Market</td><td>5</td><td>5</td><td>5</td><td>5</td><td><span class="buy">Buy Now</span></td><td><svg width="18" height="18" viewBox="0 0 24 24"><path d="M2 10h4v12H2zM8 22h10l3-9v-3h-7l1-5-2-3-5 8z" fill="#5e0b0b"/></svg></td></tr>
    <tr><td class="product"><div class="product-cell"><span class="thumb dark" role="img" aria-label="Product photo"></span><div><div class="pname">Harbor Lane Tobacco</div><div class="maker">-Bristle Baron</div></div></div></td><td>USA</td><td>Jojoba,</td><td>Spice Market</td><td>5</td><td>5</td><td>5</td><td>5</td><td><span class="buy">Buy Now</span></td><td><svg width="18" height="18" viewBox="0 0 24 24"><path d="M2 10h4v12H2zM8 22h10l3-9v-3h-7l1-5-2-3-5 8z" fill="#5e0b0b"/></svg></td></tr>
    <tr><td class="product"><div class="product-cell"><span class="thumb" role="img" aria-label="Product photo"></span><div><div class="pname">Ridge-Ranger</div><div class="maker">-Bristle Baron</div></div></div></td><td>USA</td><td>Jojoba,</td><td>Spice Market</td><td>5</td><td>5</td><td>5</td><td>5</td><td><span class="buy">Buy Now</span></td><td><svg width="18" height="18" viewBox="0 0 24 24"><path d="M2 10h4v12H2zM8 22h10l3-9v-3h-7l1-5-2-3-5 8z" fill="#5e0b0b"/></svg></td></tr>
  </tbody>
</table>

<div class="abs loading"><svg width="16" height="16" viewBox="0 0 16 16"><path d="M8 2a6 6 0 1 1-6 6" fill="none" stroke="#fff" stroke-width="2" stroke-dasharray="3 2"/></svg>Loading More...</div>

<aside>
  <div class="abs subscribe">
    <h3>Get More Stuff Like<br>This In Your InBox</h3>
    <p>Subscribe to our mailing list &amp; get interesting stuff &amp; updates.</p>
    <div class="field">Enter your email here</div>
    <div class="signup">SIGNUP NOW</div>
    <small>We respect your privacy and take protecting it seriously</small>
  </div>
  <div class="abs blog-title">Latest Blog</div>
  <article class="post" style="top:1452px"><div class="shot" role="img" aria-label="Photo of a beard oil pouch on a wooden table"></div><h4>Foggy Peak Beard Oil by Papa Hale Grooming</h4><time>February 12, 2016</time></article>
  <article class="post" style="top:1710px"><div class="shot" role="img" aria-label="Close-up photo of a glass dropper with oil" style="background:linear-gradient(135deg,#6f8a6a,#2f3f2e)"></div><h4>Outback Face/Beard Oil by Wholehand Soaps</h4><time>February 9, 2016</time></article>
  <article class="post" style="top:1960px"><div class="shot" role="img" aria-label="Photo of a wrapped beard oil bottle on a table" style="background:linear-gradient(135deg,#b48a60,#6a4a2e)"></div><h4>Clipstone Beard Oil by Clipstone Men's Grooming</h4><time>January 25, 2016</time></article>
  <article class="post" style="top:2211px"><div class="shot" role="img" aria-label="Photo of a small dark beard oil bottle" style="background:linear-gradient(135deg,#d8d2c4,#4a4038)"></div><h4>Timberline Oil by Allied Beard Co.</h4><time>January 10, 2016</time></article>
</aside>

<footer class="abs footer">
  <span>Copyright 2016 Top Whisker Tonic. All Rights Reserved.</span>
  <div class="socials" aria-label="Social links"><span></span><span></span><span></span><span></span></div>
</footer>
</body>
</html>
```